Junk Removal Truck Wrap Design

We are looking for a wrap for our new trucks that is RACING inspired. Just like real race cars our junk removal dump trucks will have sponsors who advertise on the front, sides, and rear of the truck. My vision is for the top 2/3 of the truck bed to be the "Swift Fern Haulers" logo & phone number. The lower 1/3 will be 4 or 5 spaces for sponsor logos. The rear of the truck will need to display our business logo and phone number as well; but ideally should retain space for at least 3 or 4 sponsorship logos too. I have included images of race cars and trucks that really catch my attention so you may include elements if you so desire. I like the GREEN thick stripe / GREEN thin stripe that Valtorini racing uses etc...
Our company's objective is to help people get rid of their unwanted items as quickly as possible while providing friendly service at a fair price; our trucks are often the first impression that people get and we hope to convey this message to potential customers through effective design.

Target Market(s)

The race-inspired theme should have broad appeal whether the customer enjoys the sports of auto racing or has ever pondered attending a racing event; but ultimately the racing theme gets the idea across that we will remove your stuff / junk in a hurry

Requirements
Must have
• Green and black as seen in our logo
Nice to have
• Would be nice to have examples of where sponsor logos could be located

```html
<!DOCTYPE html>
<html lang="en">
<head>
<meta charset="utf-8">
<title>Swift Fern Haulers – Rear Truck Wrap</title>
<link rel="stylesheet" href="https://fonts.googleapis.com/css2?family=Oswald:wght@700&family=EB+Garamond:wght@500&display=swap">
<style>
  :root {
    --page-bg: #2a2a2a;
    --sheet: #ffffff;
    --sheet-edge: #111111;
    --outline: #9a9a9a;
    --stripe-green: #129447;
    --pattern-green: #1f8a45;
    --pattern-green-light: #3cb44b;
    --ink: #222222;
    --sponsor-grey: #b8b8b8;
    --lamp-red: #ff0000;
    --lamp-ring: #000000;
  }
  html, body {
    margin: 0;
    width: 1200px;
    height: 1181px;
    overflow: hidden;
    background: var(--page-bg);
  }
  .wrap-sheet {
    position: absolute;
    left: 37px;
    top: 230px;
    width: 1125px;
    height: 720px;
    display: block;
  }
  .sheet-bg { fill: var(--sheet); stroke: var(--sheet-edge); stroke-width: 2; }
  .truck-outline, .panel-cell { fill: none; stroke: var(--outline); stroke-width: 2; }
  .stripe { fill: var(--stripe-green); }
  .race-pattern { fill: url(#patternTone); }
  .brand-name {
    font-family: 'Oswald', sans-serif;
    font-weight: 700;
    font-size: 34px;
    fill: var(--ink);
  }
  .brand-phone {
    font-family: 'Oswald', sans-serif;
    font-weight: 700;
    font-size: 58px;
    fill: var(--ink);
  }
  .sponsor-slot {
    font-family: 'EB Garamond', serif;
    font-weight: 500;
    font-size: 44px;
    fill: var(--sponsor-grey);
  }
  .tail-lamp { fill: var(--lamp-red); stroke: var(--lamp-ring); stroke-width: 6; }
</style>
</head>
<body>
<svg class="wrap-sheet" viewBox="155 284 1125 720" xmlns="http://www.w3.org/2000/svg">
  <defs>
    <linearGradient id="patternTone" x1="0" y1="0" x2="1" y2="0">
      <stop offset="0" stop-color="#1f8a45"/>
      <stop offset="0.5" stop-color="#3cb44b"/>
      <stop offset="1" stop-color="#1f8a45"/>
    </linearGradient>
  </defs>

  <rect class="sheet-bg" x="155" y="284" width="1125" height="720"/>

  <!-- Truck rear body -->
  <rect class="truck-outline" x="220" y="345" width="1004" height="603"/>

  <!-- Racing stripes -->
  <g class="stripes">
    <rect class="stripe" x="228" y="345" width="40" height="519"/>
    <rect class="stripe" x="284" y="345" width="8" height="519"/>
    <rect class="stripe" x="651" y="345" width="42" height="519"/>
    <rect class="stripe" x="709" y="345" width="7" height="519"/>
    <rect class="stripe" x="730" y="345" width="7" height="519"/>
    <rect class="stripe" x="756" y="345" width="42" height="519"/>
    <rect class="stripe" x="1150" y="345" width="7" height="519"/>
    <rect class="stripe" x="1175" y="345" width="40" height="519"/>
  </g>

  <!-- Left door panels -->
  <g class="door door-left">
    <rect class="panel-cell" x="301" y="345" width="346" height="80"/>
    <rect class="panel-cell" x="301" y="425" width="346" height="146"/>
    <rect class="panel-cell" x="301" y="571" width="346" height="80"/>
    <rect class="panel-cell" x="301" y="651" width="346" height="134"/>
    <rect class="panel-cell" x="301" y="785" width="346" height="79"/>

    <rect class="race-pattern" x="320" y="352" width="308" height="66" role="img" aria-label="Checkered flag and chevron racing pattern"/>
    <rect class="race-pattern" x="320" y="578" width="308" height="66" role="img" aria-label="Checkered flag and chevron racing pattern"/>
    <rect class="race-pattern" x="316" y="792" width="310" height="66" role="img" aria-label="Checkered flag and chevron racing pattern"/>

    <text class="brand-name" x="474" y="474" text-anchor="middle">SWIFT FERN HAULERS</text>
    <text class="brand-phone" x="474" y="555" text-anchor="middle">555-310-0187</text>
    <text class="sponsor-slot" x="479" y="726" text-anchor="middle">sponsor logo</text>
  </g>

  <!-- Right door panels -->
  <g class="door door-right">
    <rect class="panel-cell" x="798" y="345" width="345" height="80"/>
    <rect class="panel-cell" x="798" y="425" width="345" height="146"/>
    <rect class="panel-cell" x="798" y="571" width="345" height="80"/>
    <rect class="panel-cell" x="798" y="651" width="345" height="134"/>
    <rect class="panel-cell" x="798" y="785" width="345" height="79"/>

    <rect class="race-pattern" x="818" y="352" width="306" height="66" role="img" aria-label="Checkered flag and chevron racing pattern"/>
    <rect class="race-pattern" x="818" y="578" width="306" height="66" role="img" aria-label="Checkered flag and chevron racing pattern"/>
    <rect class="race-pattern" x="818" y="792" width="306" height="66" role="img" aria-label="Checkered flag and chevron racing pattern"/>

    <text class="sponsor-slot" x="966" y="512" text-anchor="middle">sponsor logo</text>
    <text class="sponsor-slot" x="972" y="729" text-anchor="middle">sponsor logo</text>
  </g>

  <!-- Bumper with tail lamps -->
  <g class="bumper">
    <rect class="panel-cell" x="220" y="864" width="1004" height="84"/>
    <circle class="tail-lamp" cx="265" cy="908" r="21"/>
    <circle class="tail-lamp" cx="671" cy="908" r="21"/>
    <circle class="tail-lamp" cx="721" cy="908" r="21"/>
    <circle class="tail-lamp" cx="773" cy="908" r="21"/>
    <circle class="tail-lamp" cx="1184" cy="908" r="21"/>
  </g>
</svg>
</body>
</html>
```